Wedding Marloes & Joost - Save the Date Wedding Card

I would like to have a creative save the date wedding card. We like grey/black/white colors and modern/ plain and simple.
I like the Save the Date copy big and book a flight copy smaller. I like stylish fonts for the save the date copy
Copy front:
Save the Date & book a flight
7-10-2017 Denia (Spanje)
Marloes & Joost
Onze dag is niet compleet zonder jou!
Copy back:
6-10 preferred travel date
7-10 wedding ceremony/drinks/dinner/party
8-10 hangover breakfast
Nearest Airports Valencia & Alicante
More info will be available soon!
Target Market(s)
wedding guests
Industry/Entity Type
Wedding

```html
<!DOCTYPE html>
<html lang="en">
<head>
<meta charset="utf-8">
<title>Save the Date – Travel Details</title>
<link rel="stylesheet" href="https://fonts.googleapis.com/css2?family=Parisienne&display=swap">
<style>
  :root {
    --paper: #f5f0e6;
    --gold: #9c8a63;
    --ink: #5a5040;
    --ornament-tone: rgba(156, 138, 99, 0.22);
  }
  html, body {
    margin: 0;
    padding: 0;
    overflow: hidden;
    background: var(--paper);
  }
  .card {
    position: relative;
    width: 1076px;
    height: 1200px;
    background: var(--paper);
    overflow: hidden;
  }
  .frame {
    position: absolute;
    inset: 0;
  }
  .details {
    position: absolute;
    left: 0;
    right: 0;
    top: 318px;
    text-align: center;
    font-family: "Parisienne", cursive;
    font-size: 46px;
    line-height: 67px;
    color: var(--gold);
    letter-spacing: 1px;
  }
  .details p { margin: 0; }
  .date { color: var(--ink); }
  .gap { height: 64px; }
  .closing { color: var(--ink); }
</style>
</head>
<body>
<main class="card">
  <svg class="frame" width="1076" height="1200" viewBox="0 0 1076 1200" fill="none" stroke="var(--gold)">
    <!-- double border lines -->
    <g stroke-width="1.5">
      <line x1="140" y1="150" x2="480" y2="150"/>
      <line x1="596" y1="150" x2="936" y2="150"/>
      <line x1="140" y1="1048" x2="480" y2="1048"/>
      <line x1="596" y1="1048" x2="936" y2="1048"/>
      <line x1="160" y1="130" x2="330" y2="130"/>
      <line x1="746" y1="130" x2="916" y2="130"/>
      <line x1="160" y1="1068" x2="330" y2="1068"/>
      <line x1="746" y1="1068" x2="916" y2="1068"/>
      <line x1="73" y1="210" x2="73" y2="540"/>
      <line x1="73" y1="660" x2="73" y2="990"/>
      <line x1="1003" y1="210" x2="1003" y2="540"/>
      <line x1="1003" y1="660" x2="1003" y2="990"/>
      <line x1="105" y1="200" x2="105" y2="335"/>
      <line x1="105" y1="865" x2="105" y2="1000"/>
      <line x1="971" y1="200" x2="971" y2="335"/>
      <line x1="971" y1="865" x2="971" y2="1000"/>
    </g>
    <g stroke-width="3">
      <line x1="307" y1="141" x2="500" y2="141"/>
      <line x1="576" y1="141" x2="769" y2="141"/>
      <line x1="307" y1="1057" x2="500" y2="1057"/>
      <line x1="576" y1="1057" x2="769" y2="1057"/>
      <line x1="82" y1="370" x2="82" y2="530"/>
      <line x1="82" y1="670" x2="82" y2="830"/>
      <line x1="994" y1="370" x2="994" y2="530"/>
      <line x1="994" y1="670" x2="994" y2="830"/>
    </g>
    <!-- ornament placeholders -->
    <g fill="var(--ornament-tone)" stroke="none">
      <rect role="img" aria-label="Scrolled corner flourish, top left" x="20" y="74" width="118" height="118" rx="40"/>
      <rect role="img" aria-label="Scrolled corner flourish, top right" x="938" y="74" width="118" height="118" rx="40"/>
      <rect role="img" aria-label="Scrolled corner flourish, bottom left" x="20" y="1006" width="118" height="118" rx="40"/>
      <rect role="img" aria-label="Scrolled corner flourish, bottom right" x="938" y="1006" width="118" height="118" rx="40"/>
      <rect role="img" aria-label="Scrolled centre flourish, top" x="496" y="84" width="84" height="68" rx="30"/>
      <rect role="img" aria-label="Scrolled centre flourish, bottom" x="496" y="1046" width="84" height="68" rx="30"/>
      <rect role="img" aria-label="Scrolled side flourish, left" x="22" y="550" width="68" height="100" rx="30"/>
      <rect role="img" aria-label="Scrolled side flourish, right" x="986" y="550" width="68" height="100" rx="30"/>
    </g>
  </svg>

  <section class="details">
    <p><span class="date">6-10</span> Preferred travel date</p>
    <p><span class="date">7-10</span> Wedding</p>
    <p>ceremony/drinks/dinner/party</p>
    <p><span class="date">8-10</span> Hangover lunch</p>
    <div class="gap"></div>
    <p>Nearest Airports Valencia &amp; Alicante</p>
    <p class="closing">More info will be available soon!</p>
  </section>
</main>
</body>
</html>
```